Dental Office Business Card

We need a business card for our pediatric dentistry office.
On one side the design needs to contain the following:
our logo (attached)
Vento Pediatric Grins
Soraya Kadbelani, DDS
Board Certified Pediatric Dentist
Tel: (555) 318-2747)
Fax: (555) 264-8031
Email: info@ventopediatricgrins.example
Web: www.ventopediatricgrins.example
Address: 41 Brindle Ave, Suite 208, Wellesley, MA 02099

On the other side of the card, the design needs to have an appointment reminder (date and time as well as day of the week) similar to the design attached (no need for appointment reason “For”)

```html
<!DOCTYPE html>
<html lang="en">
<head>
<meta charset="utf-8">
<title>Vento Pediatric Grins – Business Card</title>
<link rel="stylesheet" href="https://fonts.googleapis.com/css2?family=Montserrat:wght@400;500;600;700&family=Poppins:ital,wght@0,400;0,500;1,400&display=swap">
<style>
  :root {
    --backdrop: #3b3b3b;
    --card-dark: #1f1f1f;
    --card-light: #ffffff;
    --mint: #9fd5a7;
    --ink: #1b1b1b;
    --white: #ffffff;
  }
  * { box-sizing: border-box; margin: 0; padding: 0; }
  html, body { width: 1200px; height: 694px; overflow: hidden; }
  body {
    background: var(--backdrop);
    display: flex;
    align-items: center;
    justify-content: center;
    gap: 40px;
  }
  .card {
    width: 540px;
    height: 309px;
    border-radius: 22px;
    position: relative;
    overflow: hidden;
  }

  /* Appointment side */
  .appointment {
    background: var(--card-light);
    color: var(--ink);
    font-family: "Poppins", sans-serif;
    padding: 34px 34px 0;
  }
  .appointment-title {
    font-family: "Montserrat", sans-serif;
    font-weight: 700;
    font-size: 24px;
    letter-spacing: 1px;
    color: var(--mint);
    text-align: center;
    margin-bottom: 30px;
  }
  .field-row { display: flex; align-items: flex-end; gap: 18px; margin-bottom: 22px; }
  .field { display: flex; align-items: flex-end; flex: 1; font-size: 14px; }
  .field-label { white-space: nowrap; margin-right: 6px; }
  .field-line { flex: 1; border-bottom: 1px solid var(--ink); height: 16px; }
  .field-date { flex: 1.55; }
  .weekdays {
    display: flex;
    justify-content: space-between;
    margin: 30px 0 32px;
    font-size: 14px;
  }
  .weekday { display: flex; align-items: center; gap: 6px; }
  .checkbox {
    width: 15px; height: 15px;
    border: 2px solid var(--mint);
    border-radius: 3px;
  }
  .notice {
    font-style: italic;
    font-size: 9.6px;
    text-align: center;
    white-space: nowrap;
    margin: 0 -14px;
  }

  /* Contact side */
  .contact {
    background: var(--card-dark);
    color: var(--white);
    font-family: "Montserrat", sans-serif;
    display: flex;
    align-items: center;
  }
  .brand {
    width: 262px;
    display: flex;
    align-items: center;
    justify-content: center;
    gap: 10px;
    padding-left: 14px;
  }
  .brand-dot {
    width: 30px; height: 30px;
    border-radius: 50%;
    background: var(--mint);
    flex: none;
  }
  .brand-name {
    font-weight: 700;
    font-size: 22px;
    line-height: 1.15;
    color: var(--white);
  }
  .divider {
    width: 1px;
    height: 190px;
    background: var(--mint);
    flex: none;
  }
  .details { padding-left: 22px; font-size: 11.5px; line-height: 1.45; }
  .practice-name {
    font-weight: 700;
    font-size: 16px;
    color: var(--mint);
    margin-bottom: 2px;
  }
  .details-group { margin-bottom: 9px; }
  .contact-line { display: flex; align-items: center; gap: 7px; }
  .contact-line svg { width: 11px; height: 11px; fill: var(--mint); flex: none; }
</style>
</head>
<body>

  <section class="card appointment" aria-label="Appointment reminder side">
    <h2 class="appointment-title">YOUR NEXT APPOINTMENT</h2>
    <div class="field-row">
      <div class="field"><span class="field-label">Name :</span><span class="field-line"></span></div>
    </div>
    <div class="field-row">
      <div class="field field-date"><span class="field-label">Date :</span><span class="field-line"></span></div>
      <div class="field"><span class="field-label">Time :</span><span class="field-line"></span></div>
    </div>
    <div class="weekdays">
      <span class="weekday"><span class="checkbox"></span>Mon</span>
      <span class="weekday"><span class="checkbox"></span>Tue</span>
      <span class="weekday"><span class="checkbox"></span>Wed</span>
      <span class="weekday"><span class="checkbox"></span>Thu</span>
      <span class="weekday"><span class="checkbox"></span>Fri</span>
      <span class="weekday"><span class="checkbox"></span>Sat</span>
      <span class="weekday"><span class="checkbox"></span>Sun</span>
    </div>
    <p class="notice">If you are unable to keep your Appointment, please let us know at least 24 hours in advance</p>
  </section>

  <section class="card contact" aria-label="Contact side">
    <div class="brand">
      <span class="brand-dot"></span>
      <span class="brand-name">Vento Pediatric Grins</span>
    </div>
    <div class="divider"></div>
    <div class="details">
      <div class="details-group">
        <p class="practice-name">Vento Pediatric Grins</p>
        <p>Soraya Kadbelani, DDS</p>
        <p>Board Certified Pediatric Dentist</p>
      </div>
      <div class="details-group">
        <p>41 Brindle Ave, Suite 208</p>
        <p>Fernvale, NH 02099</p>
      </div>
      <div>
        <p class="contact-line">
          <svg viewBox="0 0 24 24" aria-hidden="true"><path d="M6.6 10.8a15.5 15.5 0 0 0 6.6 6.6l2.2-2.2c.3-.3.7-.4 1-.2 1.1.4 2.3.6 3.6.6.6 0 1 .4 1 1V20c0 .6-.4 1-1 1A17 17 0 0 1 3 4c0-.6.4-1 1-1h3.5c.6 0 1 .4 1 1 0 1.3.2 2.5.6 3.6.1.3 0 .7-.2 1z"/></svg>
          (555) 318-2747
        </p>
        <p class="contact-line">
          <svg viewBox="0 0 24 24" aria-hidden="true"><path d="M6 2h12v6H6zM4 9h16a2 2 0 0 1 2 2v6h-4v5H6v-5H2v-6a2 2 0 0 1 2-2zm4 8v3h8v-3z"/></svg>
          (555) 264-8031
        </p>
        <p class="contact-line">
          <svg viewBox="0 0 24 24" aria-hidden="true"><path d="M2 5h20v14H2zm2 2v.5l8 5 8-5V7z"/></svg>
          info@ventopediatricgrins.example
        </p>
        <p class="contact-line">
          <svg viewBox="0 0 24 24" aria-hidden="true"><path d="M12 2a10 10 0 1 0 0 20 10 10 0 0 0 0-20zm0 2c1 1.2 1.8 3 2.1 5H9.9C10.2 7 11 5.2 12 4zM4.3 11h3.6c0 .7 0 1.300.1 2H4.3a8 8 0 0 1 0-2zm5.6 2a16 16 0 0 1 0-2h4.2a16 16 0 0 1 0 2zm6.1 0c.1-.7.1-1.3.1-2h3.6a8 8 0 0 1 0 2zm-4 7c-1-1.2-1.8-3-2.1-5h4.2c-.3 2-1.1 3.8-2.1 5z"/></svg>
          www.ventopediatricgrins.example
        </p>
      </div>
    </div>
  </section>

</body>
</html>
```